AI Layout work for Business Cards, Letterhead and Compliment Slip for Award-winning UK Property Deve

No actual logo or corporate identity design work needed here but some skill required to create layouts for business card, letterhead and compliment slip for this award-winning company.
I can provide AI files featuring the company logo and an initial layout of the business card, (6 versions featuring the same design but for different personnel), along with some initial instructions (with possibly more to follow from the client). The finished layouts for each item need to be print-ready in AI format - 8 in all (6 for each business card plus 1 for letterhead and 1 for compliment slip).
I've given this project a 5-day duration but there may be some flexibility built into that depending on client feedback. Hopefully that won't be a problem.
UPDATE:
The client has been very prescriptive about the layout and design of these. To that end, please find 3 additional pdfs that explain what's required.
1.
All BUSINESS CARDS need to be laid out as per the attached AI file (but see latest pdf to check which layout - there are 2 in the original AI file). Use the details in the RUNE-contact-details.pdf to create 6 individual AI files, one for each card.
2.
Create 2 additional AI files, one each for the LETTERHEAD and the COMPLIMENT SLIP based on the latest mock-up that I've provided (letterhead-layout-final.pdf)
In all, I need EIGHT individual AI files, 6 for each business card, 1 for the letterhead and 1 for the compliment slip. I'd like to get this done as soon as possible now please.
Target Market(s)
Purchasers of upmarket luxury properties - see here: http://www.runeestates.co.uk
Industry/Entity Type
Business
Requirements
Must have
- Layouts need to be cool, understated and uncluttered.
Nice to have
- Please keep it simple! The actual logo background colour is likely to change (awaiting confirmation from client) but accompanying text detail and font (Deja Vu Sans Condensed) can remain as seen in the files below - for the time being at least! That having been said, I'm open to suggestions.
Should not have
- Nothing extreme or ostentatious please.

```html
<!DOCTYPE html>
<html lang="en">
<head>
<meta charset="utf-8">
<title>RUNE Urban Properties – Compliment Slip</title>
<link rel="stylesheet" href="https://fonts.googleapis.com/css2?family=Lato:wght@300;400;700&display=swap">
<style>
  :root {
    --backdrop: #c9c9c9;
    --paper: #ffffff;
    --navy: #1b2159;
    --navy-deep: #141a4d;
    --tile-dark: #4b5287;
    --tile-light: #c9cbdc;
    --band-text: #ffffff;
    --band-subtext: #aeb2d0;
  }
  * { box-sizing: border-box; margin: 0; padding: 0; }
  html, body {
    width: 1200px;
    height: 1000px;
    overflow: hidden;
    background: var(--backdrop);
    font-family: "Lato", Arial, sans-serif;
  }
  .canvas {
    position: relative;
    width: 1200px;
    height: 1000px;
    display: flex;
    align-items: center;
    justify-content: center;
  }
  .compliment-slip {
    position: relative;
    width: 960px;
    height: 452px;
    background: var(--paper);
    box-shadow: 0 10px 30px rgba(0, 0, 0, 0.18);
    overflow: hidden;
  }
  .brand-block {
    position: absolute;
    left: 0;
    top: 0;
    width: 250px;
    height: 140px;
    padding: 24px 28px;
    background: var(--navy);
    display: flex;
    align-items: center;
    justify-content: center;
  }
  .brand-name {
    display: flex;
    flex-direction: column;
    align-items: center;
    gap: 6px;
    color: var(--band-text);
    font-weight: 400;
    font-size: 16px;
    line-height: 1.2;
    letter-spacing: 1.5px;
    text-transform: uppercase;
    text-align: center;
    white-space: nowrap;
  }
  .tile-motif {
    position: absolute;
    right: 0;
    top: 0;
    width: 210px;
    height: 112px;
  }
  .contact-band {
    position: absolute;
    left: 0;
    bottom: 0;
    width: 100%;
    height: 122px;
    padding: 0 40px;
    background: linear-gradient(90deg, var(--navy-deep), var(--navy));
    display: flex;
    flex-direction: column;
    align-items: center;
    justify-content: center;
    gap: 8px;
  }
  .contact-line {
    color: var(--band-text);
    font-weight: 700;
    font-size: 17px;
    letter-spacing: 0.2px;
    white-space: nowrap;
  }
  .address-line {
    color: var(--band-subtext);
    font-weight: 300;
    font-size: 15px;
    white-space: nowrap;
  }
</style>
</head>
<body>
<main class="canvas">
  <section class="compliment-slip">
    <div class="brand-block">
      <p class="brand-name"><span>RUNE</span><span>Urban Properties</span></p>
    </div>

    <svg class="tile-motif" viewBox="0 0 210 112" role="img" aria-label="Decorative grid of overlapping navy and pale blue squares">
      <defs>
        <linearGradient id="tileTone" x1="0" y1="0" x2="0" y2="1">
          <stop offset="0" stop-color="#4b5287"/>
          <stop offset="1" stop-color="#c9cbdc"/>
        </linearGradient>
      </defs>
      <rect x="0" y="0" width="210" height="112" fill="url(#tileTone)"/>
    </svg>

    <footer class="contact-band">
      <p class="contact-line">TEL: +44 (0)1632 960418 | WEB: &nbsp;www.runeestates.co.uk | EMAIL: enquiries@runeestates.co.uk</p>
      <p class="address-line">RUNE Exclusive Properties - Moor End House, Moor End Lane, Little Ashcombe, HX4 9QT</p>
    </footer>
  </section>
</main>
</body>
</html>
```